Wedding Postcard Design

We want to design a postcard using our photo's from our wedding and send the postcards as 'Thank You's' to the guests from our wedding. On the front we would like to use the 3 x photos we have uploaded and perhaps with white boarders and on the back just lines for the addresses.
Ideally we would like them slightly larger size than the standard postcard if possible.
Updates

Sorry for the change however we feel 5 photos is too many and too crowded as I am sure you would agree.  

Can we possibly reduce it to 3 photos using the following 3:

- black and white photo
- photo with the beach behind us
- close up photo on the wharf where he is standing behind me and there is a little yellow boat behind us

 

                                                                 

Target Market(s)

Our friends

Industry/Entity Type

Wedding

```html
<!DOCTYPE html>
<html lang="en">
<head>
<meta charset="utf-8">
<title>Wedding Thank You Postcard</title>
<link href="https://fonts.googleapis.com/css2?family=Cherry+Swash:wght@400;700&display=swap" rel="stylesheet">
<style>
  :root {
    --ink: #000000;
    --paper: #ffffff;
    --sky: #ece8e6;
    --sea: #d9d4d1;
    --grass: #9e9894;
    --shade: #6f6a67;
    --mono-dark: #3a3a3a;
    --mono-light: #bdbdbd;
  }
  * { box-sizing: border-box; margin: 0; padding: 0; }
  html, body {
    width: 789px; height: 1200px; overflow: hidden;
    background: var(--paper);
    font-family: "Cherry Swash", cursive;
  }
  .sheet { position: relative; width: 789px; height: 1200px; }
  .postcard {
    position: absolute; left: 46px; width: 697px; height: 539px;
    overflow: hidden; background: var(--sky);
  }
  .postcard--front { top: 33px; }
  .postcard--back { top: 609px; }
  .scene-photo {
    position: absolute; inset: 0;
    background: linear-gradient(180deg, var(--sky) 0%, var(--sky) 38%, var(--sea) 48%, var(--sea) 58%, var(--grass) 72%, var(--shade) 100%);
  }
  .postcard--back .scene-photo {
    background: linear-gradient(180deg, #f1eeec 0%, #f1eeec 38%, #e4e0dd 48%, #e0dcd9 58%, #bdb7b3 72%, #a19b97 100%);
  }
  .decor { position: absolute; inset: 0; width: 697px; height: 539px; }
  .base-band {
    position: absolute; left: 0; right: 0; bottom: 0; height: 20px;
    background: var(--ink);
  }
  .snapshot {
    position: absolute; background: var(--paper); padding: 10px;
    box-shadow: 0 0 0 1px #d0d0d0;
  }
  .snapshot__inner {
    width: 100%; height: 100%;
    border: 4px dotted var(--ink); padding: 6px;
    background: var(--paper);
  }
  .snapshot__photo { width: 100%; height: 100%; }
  .snapshot--mono { left: -6px; top: 272px; width: 192px; height: 262px; transform: rotate(3deg); }
  .snapshot--mono .snapshot__photo { background: linear-gradient(160deg, var(--mono-dark), #5a5a5a 55%, var(--mono-light)); }
  .snapshot--beach { left: 178px; top: 300px; width: 180px; height: 240px; transform: rotate(-10deg); }
  .snapshot--beach .snapshot__photo { background: linear-gradient(180deg, #e9e6e4, #b8b3b0 60%, #8d8885); }
  .snapshot--wharf { left: 330px; top: 410px; width: 200px; height: 170px; transform: rotate(-15deg); }
  .snapshot--wharf .snapshot__photo { background: linear-gradient(180deg, #d8d4d1, #8e8986); }
  .greeting {
    position: absolute; left: 362px; top: 222px; width: 330px;
    text-align: center; color: var(--ink); white-space: nowrap;
  }
  .greeting__title { font-size: 32px; font-weight: 700; line-height: 42px; }
  .greeting__line { font-size: 22px; line-height: 52px; }
  .stamp-box {
    position: absolute; left: 539px; top: 32px; width: 109px; height: 119px;
    border: 4px solid var(--ink);
  }
  .address-line {
    position: absolute; left: 43px; width: 608px; height: 3px;
    background: var(--ink);
  }
</style>
</head>
<body>
<main class="sheet">

  <section class="postcard postcard--front">
    <div class="scene-photo" role="img" aria-label="Photo of the bride and groom standing on a grassy headland above the beach"></div>

    <svg class="decor" viewBox="0 0 697 539" aria-hidden="true">
      <path d="M0 0 H697 V8 C600 28 480 56 360 66 C260 74 200 92 165 135 C135 170 80 178 0 172 Z" fill="var(--ink)"/>
      <path d="M190 92 C320 66 470 98 697 22 V52 C520 112 340 100 190 92 Z" fill="var(--ink)"/>
      <circle cx="30" cy="190" r="40" fill="var(--ink)"/>
      <circle cx="30" cy="190" r="20" fill="none" stroke="var(--paper)" stroke-width="5"/>
      <circle cx="672" cy="476" r="40" fill="var(--ink)"/>
      <circle cx="672" cy="476" r="19" fill="none" stroke="var(--paper)" stroke-width="5"/>
    </svg>

    <figure class="snapshot snapshot--mono">
      <div class="snapshot__inner"><div class="snapshot__photo" role="img" aria-label="Black and white photo of the couple walking together"></div></div>
    </figure>
    <figure class="snapshot snapshot--beach">
      <div class="snapshot__inner"><div class="snapshot__photo" role="img" aria-label="Photo of the couple with the beach behind them"></div></div>
    </figure>
    <figure class="snapshot snapshot--wharf">
      <div class="snapshot__inner"><div class="snapshot__photo" role="img" aria-label="Close-up photo of the couple on the wharf"></div></div>
    </figure>

    <div class="greeting">
      <p class="greeting__title">'Thank You's'</p>
      <p class="greeting__line">TO THE GUESTS</p>
      <p class="greeting__line">FROM OUR WEDDING</p>
    </div>

    <div class="base-band"></div>
  </section>

  <section class="postcard postcard--back">
    <div class="scene-photo" role="img" aria-label="Faded photo of the bride and groom on the headland by the beach"></div>
    <div class="stamp-box"></div>
    <div class="address-line" style="top:255px"></div>
    <div class="address-line" style="top:297px"></div>
    <div class="address-line" style="top:339px"></div>
    <div class="address-line" style="top:380px"></div>
    <div class="base-band"></div>
  </section>

</main>
</body>
</html>
```